Business Card Design

I want to pull elements/colors from Website. Attached is a screen shot. Do not want any buildings/building graphics/construction clichés. This is for a construction management firm but I want to keep it broad enough that I can expand into other areas. I do not want the logo to be limited. Thank you.
Updates

Please review the screen shot of the website. Please use the font and color of Brackwell Ventures, LLC on the website. Please use the tag line "Construction Management in the Palm Beaches" Please show contractor license ... CGC 4093615 You may use the back for the contact information. Please no phone/house icons. It does not have to be a black card. Thank you.

Target Market(s)

Professional people with money. Owners, Architects, Engineers, Developers, Real Estate Agents etc.

Industry/Entity Type

Construction

Contact Information for Business Card

Brackwell Ventures, LLC
Construction Management

Dale T Brackwell
240 Marlidge Court #14
North Palm Beach, FL 33408
(561) 555-0187
www.BrackwellVentures.example

Requirements
Must have
• Clean, crisp, modern.

Broad enough that it is not trapped into a particular industry.

My goal is to expand into different markets, different industries.

Should not have
• The back of the card should not be colored in any way. Rubs off on other cards.

Do not want any buildings/building graphics/construction clichés.

```html
<!DOCTYPE html>
<html lang="en">
<head>
<meta charset="utf-8">
<title>Brackwell Ventures, LLC — Business Card</title>
<link rel="stylesheet" href="https://fonts.googleapis.com/css2?family=Roboto+Condensed:wght@700&family=Arimo:wght@400&family=Open+Sans:wght@400;500&display=swap">
<style>
  :root {
    --backdrop: #e6e6e3;
    --card-top: #050505;
    --card-bottom: #1c1c1e;
    --swoosh: #3a3ea6;
    --white: #ffffff;
    --grey: #b3b3b3;
    --name-blue: #a4cdf0;
    --mark-blue: #2f7fc8;
  }
  * { box-sizing: border-box; margin: 0; padding: 0; }
  html, body { width: 1200px; height: 1200px; overflow: hidden; }
  body { background: var(--backdrop); position: relative; }

  .card {
    position: absolute;
    left: 122px;
    width: 956px;
    height: 559px;
    background: radial-gradient(ellipse at 45% 85%, var(--card-bottom) 0%, var(--card-top) 70%);
    overflow: hidden;
    box-shadow: 0 6px 18px rgba(0,0,0,0.25);
  }
  .card--upper { top: 24px; }
  .card--lower { top: 617px; }

  .swoosh { position: absolute; inset: 0; width: 100%; height: 100%; }
  .swoosh path { fill: var(--swoosh); }

  .company {
    position: absolute;
    left: 58px; top: 58px;
    font-family: "Roboto Condensed", "Arial Narrow", sans-serif;
    font-weight: 700;
    font-size: 41px;
    line-height: 1.2;
    letter-spacing: 0.5px;
    color: var(--white);
  }
  .tagline {
    position: absolute;
    left: 60px; top: 124px;
    width: 590px;
    font-family: "Arimo", Arial, sans-serif;
    font-size: 23px;
    line-height: 1.2;
    letter-spacing: 0.4px;
    color: var(--grey);
  }

  .brand {
    position: absolute;
    left: 686px; top: 50px;
    width: 222px;
    font-family: "Arimo", Arial, sans-serif;
    font-weight: 400;
    color: var(--white);
  }
  .brand__square {
    width: 112px; height: 112px;
    margin-bottom: 24px;
    background: var(--mark-blue);
  }
  .brand__name { font-size: 30px; line-height: 1; letter-spacing: 0.3px; }
  .brand__sub { font-size: 19px; line-height: 1.35; margin-top: 6px; letter-spacing: 0.4px; }
  .brand__rule { height: 1px; background: var(--white); margin: 3px 0 5px; width: 218px; }
  .brand__line { font-size: 12.5px; letter-spacing: 0.3px; }

  .contact {
    position: absolute;
    left: 48px; top: 318px;
    font-family: "Open Sans", "Segoe UI", sans-serif;
    color: var(--white);
  }
  .contact__name {
    font-size: 29px;
    font-weight: 500;
    line-height: 1.2;
    color: var(--name-blue);
    margin-bottom: 6px;
  }
  .contact__row {
    height: 36px;
    line-height: 36px;
    font-size: 22px;
    white-space: nowrap;
  }
</style>
</head>
<body>

<svg width="0" height="0" style="position:absolute" aria-hidden="true">
  <defs>
    <symbol id="swoosh-shape" viewBox="0 0 956 559">
      <path d="M0 134 C 200 200 430 215 600 270 C 760 325 880 450 956 556 L 956 559 C 870 468 750 360 595 292 C 430 230 220 232 0 184 Z"/>
    </symbol>
  </defs>
</svg>

<article class="card card--upper">
  <svg class="swoosh" aria-hidden="true"><use href="#swoosh-shape"/></svg>
  <h1 class="company">BRACKWELL VENTURES, LLC</h1>
  <p class="tagline">Construction Management in the Palm Beaches</p>
  <div class="brand">
    <div class="brand__square"></div>
    <div class="brand__name">BRACKWELL</div>
    <div class="brand__sub">VENTURES, LLC</div>
    <div class="brand__rule"></div>
    <div class="brand__line">CONSTRUCTION MANAGEMENT</div>
  </div>
  <div class="contact">
    <p class="contact__name">Dale T Brackwell</p>
    <p class="contact__row">240 Marlidge Court #14 North Palm Beach, FL 33408</p>
    <p class="contact__row">(561) 555-0187</p>
    <p class="contact__row">brackwellventures@mail.example</p>
    <p class="contact__row">www.BrackwellVentures.example</p>
    <p class="contact__row">License CGC 4093615</p>
  </div>
</article>

<article class="card card--lower">
  <svg class="swoosh" aria-hidden="true"><use href="#swoosh-shape"/></svg>
  <h2 class="company">BRACKWELL VENTURES, LLC</h2>
  <p class="tagline">Construction Management in the Palm Beaches</p>
  <div class="brand">
    <div class="brand__square"></div>
    <div class="brand__name">BRACKWELL</div>
    <div class="brand__sub">VENTURES, LLC</div>
    <div class="brand__rule"></div>
    <div class="brand__line">CONSTRUCTION MANAGEMENT</div>
  </div>
  <div class="contact">
    <p class="contact__name">Dale T Brackwell</p>
    <p class="contact__row">240 Marlidge Court #14 North Palm Beach, FL 33408</p>
    <p class="contact__row">(561) 555-0187</p>
    <p class="contact__row">brackwellventures@mail.example</p>
    <p class="contact__row">www.BrackwellVentures.example</p>
    <p class="contact__row">License CGC 4093615</p>
  </div>
</article>

</body>
</html>
```